Need Letterhead Design & Matching Business Card

I have a logo that I love already. But the letterhead is less than appealing and boring. I'd like a design for my letterhead which I will match with business cards. Also, I'd like to have used fonts that are generally available, as my current letterhead uses a font named "SPACE" which nobody has unless they download it...so when a Word version is forwarded, it looks awful on the receiver's screed due to not having the font. That being said, modern is the look we like and are going for.

My business is "Halloran Brightmoor PC" - a law firm specializing in representing people who have suffered catastrophic injuries or death (plane, auto, train crashes etc.).

See attached letterhead, which has all of the pertinent information. My logo is also attached in various formats.

```html
<!DOCTYPE html>
<html lang="en">
<head>
<meta charset="utf-8">
<title>Halloran Brightmoor PC — Letterhead &amp; Business Cards</title>
<link href="https://fonts.googleapis.com/css2?family=Montserrat:wght@300;400;500&display=swap" rel="stylesheet">
<style>
  :root {
    --bg: #e4e4e4;
    --paper: #ffffff;
    --ink: #1c1c1c;
    --grey-mid: #b9b9b9;
    --grey-light: #d6d6d6;
    --text-soft: #6a6a6a;
    --rule: #9a9a9a;
  }
  * { box-sizing: border-box; margin: 0; padding: 0; }
  html, body { width: 1200px; height: 900px; overflow: hidden; }
  body {
    background: var(--bg);
    font-family: "Montserrat", sans-serif;
    color: var(--ink);
    position: relative;
  }

  /* Shared brand lockup */
  .brand { display: flex; align-items: center; gap: 12px; }
  .brand-square { width: 38px; height: 38px; background: var(--ink); flex: none; }
  .brand-name {
    font-weight: 300;
    font-size: 15px;
    line-height: 1.15;
    letter-spacing: 0.32em;
    text-transform: uppercase;
    color: var(--ink);
    white-space: nowrap;
  }

  /* Letterhead */
  .letterhead {
    position: absolute;
    left: 70px; top: 40px;
    width: 634px; height: 820px;
    background: var(--paper);
    box-shadow: 0 6px 18px rgba(0,0,0,0.12);
    overflow: hidden;
  }
  .letterhead-header {
    position: absolute;
    left: 40px; right: 40px; top: 42px;
    display: flex;
    align-items: flex-end;
    justify-content: space-between;
    padding-bottom: 12px;
    border-bottom: 1px solid var(--rule);
  }
  .header-contact {
    display: flex;
    gap: 14px;
    font-size: 7.5px;
    line-height: 1.6;
    color: var(--text-soft);
  }
  .header-contact .divider { width: 1px; background: var(--rule); }
  .letterhead-band {
    position: absolute;
    left: 0; bottom: 0;
    width: 100%; height: 220px;
    background: linear-gradient(180deg, var(--grey-mid) 0%, #6e6e6e 55%, var(--ink) 100%);
  }

  /* Business cards */
  .card {
    position: absolute;
    width: 440px; height: 251px;
    background: var(--paper);
    box-shadow: 0 6px 16px rgba(0,0,0,0.14);
    overflow: hidden;
  }
  .card-front { left: 730px; top: 110px; }
  .card-back { left: 730px; top: 420px; }

  .card-front .brand { position: absolute; left: 150px; top: 34px; }
  .card-front .brand-name { font-size: 12px; }
  .card-front-band {
    position: absolute;
    left: 0; bottom: 0;
    width: 100%; height: 110px;
    background: linear-gradient(180deg, var(--grey-light) 0%, #7a7a7a 50%, var(--ink) 100%);
  }

  .card-back .brand { position: absolute; left: 22px; top: 22px; gap: 8px; }
  .card-back .brand-square { width: 26px; height: 26px; }
  .card-back .brand-name { font-size: 8px; letter-spacing: 0.22em; }
  .card-back-band {
    position: absolute;
    left: 0; bottom: 0;
    width: 170px; height: 170px;
    background: linear-gradient(135deg, var(--grey-mid) 0%, #6e6e6e 50%, var(--ink) 100%);
  }
  .card-person { position: absolute; left: 190px; top: 70px; }
  .person-name {
    font-size: 14px;
    font-weight: 400;
    letter-spacing: 0.08em;
    text-transform: uppercase;
    white-space: nowrap;
    padding-bottom: 6px;
    margin-bottom: 8px;
    border-bottom: 1px solid var(--rule);
  }
  .person-contact {
    font-size: 8.5px;
    line-height: 1.7;
    color: var(--text-soft);
  }
  .card-web {
    position: absolute;
    right: 26px; bottom: 34px;
    font-size: 8px;
    color: var(--text-soft);
    letter-spacing: 0.05em;
  }
  .social-column {
    position: absolute;
    right: 18px; top: 30px;
    display: flex;
    flex-direction: column;
    gap: 6px;
  }
  .social-box { width: 14px; height: 14px; background: var(--ink); }
</style>
</head>
<body>

  <section class="letterhead" aria-label="Letterhead">
    <header class="letterhead-header">
      <div class="brand">
        <div class="brand-square"></div>
        <div class="brand-name">Halloran<br>Brightmoor PC</div>
      </div>
      <div class="header-contact">
        <div>1200 Harbor Lane, Suite 400<br>Brentwood, CA 90049</div>
        <div class="divider"></div>
        <div>mail@halloranbrightmoor.com<br>Tel: (310) 555-0142</div>
      </div>
    </header>
    <div class="letterhead-band" role="img" aria-label="Decorative grey and black wave band along the page foot"></div>
  </section>

  <section class="card card-front" aria-label="Business card front">
    <div class="brand">
      <div class="brand-square"></div>
      <div class="brand-name">Halloran<br>Brightmoor PC</div>
    </div>
    <div class="card-front-band" role="img" aria-label="Decorative grey and black wave band across the card"></div>
  </section>

  <section class="card card-back" aria-label="Business card back">
    <div class="brand">
      <div class="brand-square"></div>
      <div class="brand-name">Halloran<br>Brightmoor PC</div>
    </div>
    <div class="card-back-band" role="img" aria-label="Decorative grey and black wave band in the lower left corner"></div>
    <div class="card-person">
      <div class="person-name">R. Daniel Okafor, Esq</div>
      <div class="person-contact">
        1200 Harbor Lane, Suite 400<br>
        Brentwood, CA 90049<br>
        (310) 555-0142
      </div>
    </div>
    <div class="social-column" aria-hidden="true">
      <div class="social-box"></div>
      <div class="social-box"></div>
      <div class="social-box"></div>
    </div>
    <div class="card-web">www.halloranbrightmoor.com</div>
  </section>

</body>
</html>
```